Harborline Capital Partners

We are a Private Equity firm that works with small companies. We have a mission of working with companies that help others in some way, shape, or form. If we feel that there is not a definitive way that the business helps others, we initiate a program of giving to others.

Target Market(s)

Our target market is small to mid size businesses. We do not have a certain business sector that we go after, but work with companies that have a niche.

Contact Information for Business Card

Currently very plain, black and white, standard print

Logo Text

Dedicated to Success

Requirements
Must have
• Want the color(s) and scheme to give off the feeling of openness to change, smart and sharp look, with a monogrammed type logo
Nice to have
• It would be nice to have a simple and look of distinction. We operate the Private Equity Firm as a virtual office and bring in best in class partners to work on projects as partners.
Should not have
• A wild and out of touch look.

```html
<!DOCTYPE html>
<html lang="en">
<head>
<meta charset="utf-8">
<title>Harborline Capital Partners – Business Card</title>
<link rel="stylesheet" href="https://fonts.googleapis.com/css2?family=Josefin+Sans:wght@400;600&display=swap">
<style>
  :root {
    --backdrop: #e8e8e8;
    --card-white: #ffffff;
    --brand-red: #e00b17;
    --ink: #1b1b1b;
    --carbon: #222222;
    --on-dark: #f2f2f2;
  }
  html, body {
    margin: 0;
    width: 1200px;
    height: 900px;
    overflow: hidden;
    background: var(--backdrop);
  }
  .stage {
    width: 1200px;
    height: 900px;
    display: flex;
    align-items: center;
    justify-content: center;
  }
  .business-card {
    width: 1000px;
    height: 570px;
    display: block;
    box-shadow: 0 18px 40px rgba(0,0,0,0.18);
    font-family: "Josefin Sans", sans-serif;
  }
  .card-face { fill: var(--card-white); }
  .accent-band { fill: var(--brand-red); }
  .contact-panel { fill: var(--carbon); }
  .wordmark-name {
    fill: var(--ink);
    font-size: 66px;
    font-weight: 600;
    letter-spacing: 1px;
  }
  .wordmark-sub {
    fill: var(--ink);
    font-size: 29px;
    font-weight: 600;
    letter-spacing: 1.5px;
  }
  .holder-name {
    fill: var(--card-white);
    font-size: 28px;
    font-weight: 400;
  }
  .holder-role {
    fill: var(--ink);
    font-size: 22px;
    font-weight: 400;
  }
  .contact-text {
    fill: var(--on-dark);
    font-size: 21px;
    font-weight: 400;
  }
  .icon-badge {
    fill: var(--ink);
    stroke: var(--brand-red);
    stroke-width: 3;
  }
  .icon-glyph {
    fill: none;
    stroke: var(--on-dark);
    stroke-width: 2.2;
    stroke-linecap: round;
    stroke-linejoin: round;
  }
</style>
</head>
<body>
<main class="stage">
  <svg class="business-card" viewBox="0 0 1000 570" xmlns="http://www.w3.org/2000/svg" aria-label="Harborline Capital Partners business card">
    <rect class="card-face" x="0" y="0" width="1000" height="570"/>

    <g class="wordmark">
      <text class="wordmark-name" x="500" y="160" text-anchor="middle">HARBORLINE</text>
      <text class="wordmark-sub" x="500" y="202" text-anchor="middle">CAPITAL PARTNERS</text>
    </g>

    <polygon class="accent-band" points="0,330 1000,278 1000,326 0,378"/>
    <g transform="rotate(-3 500 340)">
      <text class="holder-name" x="500" y="340" text-anchor="middle">Daniel Reyes</text>
      <text class="holder-role" x="500" y="380" text-anchor="middle">Manager</text>
    </g>

    <polygon class="contact-panel" points="0,440 1000,388 1000,570 0,570"/>

    <g class="contact-item" transform="translate(180 467)">
      <circle class="icon-badge" r="22"/>
      <path class="icon-glyph" d="M-7,-10 l4,-1 3,6 -3,3 c2,4 4,6 8,8 l3,-3 6,3 -1,4 c-1,2 -4,3 -7,2 c-8,-3 -13,-8 -16,-16 c-1,-3 0,-6 3,-7z"/>
    </g>
    <text class="contact-text" x="180" y="520" text-anchor="middle" transform="rotate(-3 180 520)">555 014 2290</text>

    <g class="contact-item" transform="translate(500 450)">
      <circle class="icon-badge" r="22"/>
      <g class="icon-glyph">
        <circle r="10"/>
        <ellipse rx="4.5" ry="10"/>
        <line x1="-10" y1="0" x2="10" y2="0"/>
        <line x1="-8" y1="-5.5" x2="8" y2="-5.5"/>
        <line x1="-8" y1="5.5" x2="8" y2="5.5"/>
      </g>
    </g>
    <text class="contact-text" x="500" y="503" text-anchor="middle" transform="rotate(-3 500 503)">www.harborlinecap.com</text>

    <g class="contact-item" transform="translate(815 433)">
      <circle class="icon-badge" r="22"/>
      <g class="icon-glyph">
        <rect x="-10" y="-7" width="20" height="14" rx="1"/>
        <polyline points="-10,-7 0,1 10,-7"/>
      </g>
    </g>
    <text class="contact-text" x="815" y="486" text-anchor="middle" transform="rotate(-3 815 486)">daniel.reyes@harborlinecap.com</text>
  </svg>
</main>
</body>
</html>
```